Redesign of existing website for a corporate advisory business focussed on technology

We need a redesign of our website. We are a corporate advisory business based in Sydney. Our focus is on the technology and life-science sectors. We assist our clients with capital raisings, mergers and acquisitions and other corporate transactions.

Our business is called "Harbourline Capital Advisors"
Our current website is www.harbourlinecap.com.au

I'd like to see a complete re-design of the site. (I'm happy to keep any of the existing images - but equally happy to scrap them completely and "start again".)

My preference is that the logo remain as it is. However, I would be very open to a re-colouring of the logo if it works better with a new webiste design.

The content of the website will remain the same. I'd like one additional section - "News" - which will allow us to manually post news items and which will pull in news feeds from current and past clients.

In terms of positioning / look-and-feel:

Our clients fall into two categories. I'd like the website to appeal to both:

1. The first category is: Executives from established technology or life-science companies (private or public), who engage us to assist with strategy, capital raising, corporate transactions.

2. The second category is: Entrepreneurs looking for advice in accessing angel funding or venture capital. The site should appeal to young tech-savvy entrepreneurs who are looking to engage a firm to provide such assistance.

To accomodate both target groups, the overriding feel should be one of professionalism, stability, trust and expertise. However, while the site should look fairly "corporate", I'd like it to feel contemporary and have an element of creativity and flair, reflecting the fact that our clients are often early-stage, innovative, technology companies. (I know this might be a tricky balance...)

Target Market(s)

Potential clients. Typically executives at technology or life-science companies or (more typically) entrepreneurs building their own companies

Industry/Entity Type

Business

Requirements
Must have
• 1. All content on the existing website
2. An additional section called "News" that allows us to easily add news items or articles and ideally which accepts news feeds from a handful of past and present clients
3. An ability to easily update and edit content
Should not have
• The site should not have "gimmicks". (Definitely no devices like the moving arrow in the current site!)

It should be fairly conservative, while still feeling contemporary and fresh.

```html
<!DOCTYPE html>
<html lang="en">
<head>
<meta charset="utf-8">
<title>Harbourline Capital Advisors</title>
<link href="https://fonts.googleapis.com/css2?family=Arimo:wght@400;700&display=swap" rel="stylesheet">
<style>
:root{
  --orange:#f07020;
  --orange-light:#f7931e;
  --ink:#222;
  --text:#555;
  --muted:#666;
  --page:#e4e4e4;
  --page-top:#efefef;
  --tab:#d9d9d9;
  --white:#fff;
  --icon:#666;
}
*{margin:0;padding:0;box-sizing:border-box}
html,body{width:1200px;height:1060px;overflow:hidden}
body{
  position:relative;
  font-family:"Arimo",Arial,sans-serif;
  color:var(--text);
  background:linear-gradient(180deg,var(--page-top) 0,#ececec 700px,var(--page) 730px,var(--page) 100%);
  border-top:3px solid var(--orange-light);
}
.abs{position:absolute}
.brand{left:120px;top:41px;display:flex;align-items:center;gap:13px}
.brand-dot{width:73px;height:73px;border-radius:50%;background:var(--orange)}
.brand-name{font-size:24px;color:#444;letter-spacing:.2px}
.follow{left:900px;top:55px;display:flex;align-items:center;gap:6px;font-size:12px;font-weight:700;color:#444}
.follow span{margin-right:4px}
.social-box{width:18px;height:18px;background:var(--icon);border-radius:2px}
.nav{top:118px;left:330px;display:flex;gap:6px;list-style:none}
.nav li{height:38px;padding:0 14px;display:flex;align-items:center;gap:6px;
  background:linear-gradient(#e2e2e2,#d4d4d4);border-radius:5px 5px 0 0;
  font-size:12px;font-weight:700;color:#fff;text-shadow:0 1px 0 rgba(0,0,0,.15)}
.nav li svg{fill:#fff}
.nav li.current{background:var(--white);color:#666;text-shadow:none}
.nav li.current svg{fill:#666}
.panel{left:120px;top:156px;width:960px;height:773px;background:var(--white);border-radius:6px;box-shadow:0 1px 3px rgba(0,0,0,.08)}
.hero{left:186px;top:220px;width:828px;height:252px;border-radius:8px;overflow:hidden;
  background:linear-gradient(160deg,#fafafa 0,#f0f0f0 45%,#d8d8d8 75%,#9a9a9a 100%)}
.callout{left:19px;top:18px;width:395px;height:102px;background:#f9f9f9;border-radius:4px;
  box-shadow:0 1px 4px rgba(0,0,0,.2);padding:14px 18px}
.callout h3{font-size:14px;color:var(--orange);margin-bottom:5px}
.callout p{font-size:12px;line-height:18px;color:#333}
.dots{right:10px;bottom:10px;display:flex}
.dots i{width:22px;height:22px;border-radius:50%;background:#888;border:4px solid #999;margin-left:-3px}
.dots i.on{background:#fff;border-color:#888}
.intro{left:186px;top:525px;width:520px}
.intro h1{font-size:24px;line-height:36px;color:var(--orange);font-weight:400;letter-spacing:.3px;margin-bottom:6px}
.intro p{font-size:14px;line-height:24px;margin-bottom:12px;letter-spacing:.1px}
.news{left:733px;top:512px;width:281px;height:370px;
  background:linear-gradient(90deg,#f2f2f2 0,#fff 60%);border-left:1px solid #ddd;border-top:1px solid #eee;border-radius:3px 0 0 3px}
.news h2{font-size:24px;font-weight:400;color:var(--orange);padding:16px 25px 0;height:58px;border-bottom:1px solid #e2e2e2}
.news-item{padding:18px 0 0 22px;height:156px;border-bottom:1px solid #e8e8e8}
.news-item:last-child{border-bottom:none}
.news-item time{font-size:10px;color:#555;display:block;margin-bottom:8px}
.news-item h4{font-size:14px;color:var(--ink);margin-bottom:3px;letter-spacing:.3px}
.news-item p{font-size:11px;line-height:18px;color:#222}
.more{display:inline-block;margin-top:6px;padding:5px 10px;border-radius:11px;
  background:linear-gradient(var(--orange-light),var(--orange));color:#fff;font-size:10px;letter-spacing:.8px}
.foot-head{font-size:13px;font-weight:700;color:var(--orange);top:964px}
.links{left:186px;top:986px;display:grid;grid-template-columns:145px 148px 120px;row-gap:8px;font-size:12px;font-weight:700;color:var(--muted);list-style:none}
.links li{display:flex;align-items:center;gap:4px}
.links svg{fill:var(--muted)}
.foot-social{left:624px;top:988px;display:flex;gap:6px}
.foot-brand{left:772px;top:950px;display:flex;align-items:center;gap:10px}
.foot-brand .brand-dot{width:47px;height:47px}
.foot-brand .brand-name{font-size:15px;margin-top:-22px}
.legal{right:186px;top:986px;text-align:right;font-size:10px;line-height:18px;color:var(--muted)}
</style>
</head>
<body>
<svg width="0" height="0" style="position:absolute">
  <symbol id="i-home" viewBox="0 0 12 12"><path d="M6 1 0 6h2v5h3V8h2v3h3V6h2z"/></symbol>
  <symbol id="i-pen" viewBox="0 0 12 12"><path d="M1 11l1-3 6-6 2 2-6 6zM9 1l2 2 1-1-2-2z"/></symbol>
  <symbol id="i-star" viewBox="0 0 12 12"><path d="M6 0l1.8 4 4.2.3-3.2 2.8 1 4.1L6 9 2.2 11.2l1-4.1L0 4.3 4.2 4z"/></symbol>
  <symbol id="i-user" viewBox="0 0 12 12"><circle cx="6" cy="3" r="3"/><path d="M0 12c0-4 2.5-5 6-5s6 1 6 5z"/></symbol>
  <symbol id="i-book" viewBox="0 0 12 12"><path d="M3 1h8l-2 9H1zM2 11h8v1H2z"/></symbol>
  <symbol id="i-mail" viewBox="0 0 12 12"><path d="M0 2h12v8H0zm1 1v.5l5 3 5-3V3zm0 2v4h10V5L6 8z" fill-rule="evenodd"/></symbol>
</svg>

<header>
  <div class="abs brand"><span class="brand-dot"></span><span class="brand-name">Harbourline Capital Advisors</span></div>
  <div class="abs follow"><span>Follow us on</span><i class="social-box"></i><i class="social-box"></i><i class="social-box"></i></div>
  <ul class="abs nav">
    <li class="current"><svg width="12" height="12"><use href="#i-home"/></svg>HOME</li>
    <li><svg width="12" height="12"><use href="#i-pen"/></svg>NEWS</li>
    <li><svg width="12" height="12"><use href="#i-star"/></svg>OUR SERVICES</li>
    <li><svg width="12" height="12"><use href="#i-user"/></svg>OUR TEAM</li>
    <li><svg width="12" height="12"><use href="#i-book"/></svg>OUR EXPERIENCE</li>
    <li><svg width="12" height="12"><use href="#i-mail"/></svg>CONTACT US</li>
  </ul>
</header>

<main class="abs panel"></main>

<section class="abs hero" role="img" aria-label="Growth chart illustration: rising yellow-to-orange line with numbered phase markers on a grey grid">
  <div class="abs callout">
    <h3>Phase 3 - Lorem ipsum</h3>
    <p>Dolor sit amet, consectetuer adipiscing elit. Donec odio. Quisque volutpat mattis eros. Nullam malesuada erat ut turpis. Urna nibh, viverra non, semper suscipit, posuere a, pede.</p>
  </div>
  <div class="abs dots"><i></i><i></i><i class="on"></i></div>
</section>

<article class="abs intro">
  <h1>A corporate advisory firm with a focus on life-science and technology</h1>
  <p>Harbourline Capital Advisors is a specialist corporate advisory and investment firm with a focus on high growth companies in the Australian life-science and technology sectors.</p>
  <p>Our team combines extensive investment banking and funds management experience with sector expertise and longstanding investor relationships.</p>
  <p>Our advisory work incorporates both equity capital markets as well as mergers and acquisitions. Via our alliance with specialist US investment bank Calder Ridge Partners LLC, we are well placed to introduce qualified international partnering opportunities to our domestic clients and to provide seamless cross-border transaction execution capabilities.</p>
</article>

<aside class="abs news">
  <h2>Latest News</h2>
  <div class="news-item">
    <time>Tuesday, July 13th, 2010</time>
    <h4>Lorem Ipsum set dolor</h4>
    <p>Sed egestas, ante et vulputate volutpat, eros pede semper est, vitae luctus metus libero eu augue. Morbi purus libero, faucibus adipiscing, commodo quis.</p>
    <span class="more">READ MORE</span>
  </div>
  <div class="news-item">
    <time>Tuesday, July 13th, 2010</time>
    <h4>Lorem Ipsum set dolor</h4>
    <p>Sed egestas, ante et vulputate volutpat, eros pede semper est, vitae luctus metus libero eu augue. Morbi purus libero, faucibus adipiscing, commodo quis.</p>
    <span class="more">READ MORE</span>
  </div>
</aside>

<footer>
  <div class="abs foot-head" style="left:186px">QUICK LINKS</div>
  <ul class="abs links">
    <li><svg width="12" height="12"><use href="#i-home"/></svg>Home</li>
    <li><svg width="12" height="12"><use href="#i-pen"/></svg>News</li>
    <li><svg width="12" height="12"><use href="#i-star"/></svg>Our Services</li>
    <li><svg width="12" height="12"><use href="#i-user"/></svg>Our Team</li>
    <li><svg width="12" height="12"><use href="#i-book"/></svg>Our Experience</li>
    <li><svg width="12" height="12"><use href="#i-mail"/></svg>Contact Us</li>
  </ul>
  <div class="abs foot-head" style="left:624px">FOLLOW US ON</div>
  <div class="abs foot-social"><i class="social-box"></i><i class="social-box"></i><i class="social-box"></i></div>
  <div class="abs foot-brand"><span class="brand-dot"></span><span class="brand-name">Harbourline Capital Advisors</span></div>
  <div class="abs legal">© Harbourline Capital Advisors Pty Ltd 2011<br>AFS License No: 512907</div>
</footer>
</body>
</html>
```